Tailbrook Website Design

Need a website for a Dog Grooiming business. Please make it simular to these:

https://www.furvanto.com
https://haulnorix.com
https://meadowpetrin.com
https://www.drivelumo.com/search/

```html
<!DOCTYPE html>
<html lang="en">
<head>
<meta charset="utf-8">
<title>Tailbrook — Doorstep Dog Grooming</title>
<link rel="stylesheet" href="https://fonts.googleapis.com/css2?family=Montserrat:wght@500;600;700;800&family=Oswald:wght@400;500&family=Open+Sans:ital,wght@0,400;0,600;1,400&family=Yellowtail&display=swap">
<style>
:root{
  --blue:#1a86f0;
  --blue-deep:#1468d6;
  --green:#36b84f;
  --green-bright:#3ecf62;
  --navy:#0f3b68;
  --ink:#4d5866;
  --muted:#6f7a86;
  --pale:#f3f7fa;
  --white:#ffffff;
  --star:#f7a21b;
}
*{box-sizing:border-box;margin:0;padding:0}
html,body{width:1200px;height:4304px;overflow:hidden;background:var(--white)}
body{font-family:"Open Sans",sans-serif;color:var(--ink)}
.page{position:relative;width:1200px;height:4304px;overflow:hidden}
.abs{position:absolute}
.ph{position:absolute}

/* hero + about */
.hero{position:absolute;left:0;top:0;width:1200px;height:1228px;
  background:linear-gradient(168deg,#1a88ff 0%,#1f95f4 28%,#2fb8a0 45%,#3acb68 58%,#36c25c 100%)}
.logo{left:130px;top:20px;font-family:"Montserrat",sans-serif;font-weight:700;font-size:30px;color:var(--white)}
.nav{top:30px;font-family:"Oswald",sans-serif;font-size:14px;color:var(--white);letter-spacing:.3px}
.nav.active::after{content:"";position:absolute;left:0;right:0;top:28px;height:3px;background:var(--white)}
.call-pill{left:886px;top:20px;width:214px;height:40px;border-radius:20px;background:var(--green-bright);
  color:var(--white);font-family:"Oswald",sans-serif;font-size:15px;display:flex;align-items:center;justify-content:center;gap:6px}
.call-pill b{font-weight:500}
.script{font-family:"Yellowtail",cursive;color:var(--white)}
.hero-kicker{left:130px;top:212px;font-size:32px}
.hero-title{left:128px;top:246px;font-family:"Montserrat",sans-serif;font-weight:800;font-size:56px;line-height:62px;color:var(--white)}
.hero-sub{left:135px;top:390px;font-family:"Montserrat",sans-serif;font-weight:600;font-size:20px;line-height:25px;color:var(--white)}
.btn{display:flex;align-items:center;justify-content:center;border-radius:24px;font-family:"Oswald",sans-serif;
  font-weight:500;font-size:15px;letter-spacing:1.5px;color:var(--white);text-transform:uppercase}
.btn-green{background:var(--green-bright)}
.btn-blue{background:var(--blue)}
.btn-navy{background:var(--navy)}
.btn-outline{border:2px solid var(--white)}
.about-kicker{left:643px;top:846px;font-size:30px}
.about-title{left:636px;top:876px;font-family:"Montserrat",sans-serif;font-weight:700;font-size:44px;color:var(--white)}
.about-text{left:636px;top:946px;width:455px;font-size:15px;line-height:25px;color:var(--white)}
.about-text p+p{margin-top:4px}

.features{position:absolute;left:0;top:1228px;width:1200px;height:112px;background:var(--green);border-top:1px solid rgba(255,255,255,.35)}
.feat{position:absolute;top:40px;display:flex;align-items:center;gap:14px;color:var(--white);
  font-family:"Montserrat",sans-serif;font-weight:500;font-size:14px;line-height:17px;text-transform:uppercase}

/* video */
.video-sec{position:absolute;left:0;top:1340px;width:1200px;height:518px;background:var(--pale)}
.h-blue{font-family:"Montserrat",sans-serif;font-weight:700;color:var(--blue)}
.body-text{font-size:15px;line-height:25px;color:var(--ink)}

/* services */
.sec-title{font-family:"Montserrat",sans-serif;font-weight:700;font-size:34px;color:var(--navy);text-align:center}
.sec-title span{color:var(--green)}
.svc{position:absolute;width:248px;height:248px;border-radius:50%;color:var(--white);text-align:center}
.svc.green{background:var(--green)}
.svc.blue{background:var(--blue)}
.svc .ic{position:absolute;left:81px;top:14px;width:86px;height:86px;border-radius:50%;display:flex;align-items:center;justify-content:center}
.svc.green .ic{background:#46c462}
.svc.blue .ic{background:var(--blue-deep)}
.svc h3{position:absolute;left:20px;right:20px;top:120px;font-family:"Montserrat",sans-serif;font-weight:700;font-size:13px;line-height:21px}
.svc p{position:absolute;left:30px;right:30px;top:164px;font-size:12px;line-height:17px}

/* why */
.why-title{left:687px;top:2428px;font-family:"Montserrat",sans-serif;font-weight:700;font-size:32px;color:var(--white)}
.why-text{left:687px;top:2484px;width:390px;font-size:12.5px;line-height:21px;color:var(--white)}
.why-item{position:absolute;display:flex;align-items:center;gap:14px;color:var(--white);
  font-family:"Montserrat",sans-serif;font-weight:500;font-size:14px;line-height:17px;text-transform:uppercase}
.why-ic{width:68px;height:68px;border-radius:50%;background:var(--white);display:flex;align-items:center;justify-content:center}

/* testimonials */
.card{position:absolute;width:313px;height:228px;background:var(--white);border:2px solid #dfe3e8}
.card p{position:absolute;left:36px;right:24px;top:34px;font-style:italic;font-size:12px;line-height:18px;color:var(--muted)}
.avatar{position:absolute;left:34px;top:155px;width:36px;height:36px;border-radius:50%;background:linear-gradient(#e9b58e,#c77b55)}
.who{position:absolute;left:80px;top:155px;font-family:"Montserrat",sans-serif;font-weight:700;font-size:10.5px;color:var(--blue)}
.stars{position:absolute;left:80px;top:169px;font-size:17px;letter-spacing:1px;color:var(--star)}

/* booking */
.book{position:absolute;left:0;top:3350px;width:1200px;height:568px;background:linear-gradient(180deg,#1c86f2 0%,#2a95f5 60%,#1e88ee 100%)}
.book-title{left:0;width:1200px;top:3452px;text-align:center;font-family:"Montserrat",sans-serif;font-weight:700;font-size:34px;color:var(--white)}
.book-text{left:270px;width:660px;top:3508px;text-align:center;font-size:13px;line-height:22px;color:var(--white)}

/* footer */
.footer{position:absolute;left:0;top:3918px;width:1200px;height:386px;background:var(--pale)}
.f-head{font-family:"Montserrat",sans-serif;font-weight:600;font-size:15px;color:var(--navy)}
.f-head::after{content:"";display:block;width:38px;height:2px;background:var(--green);margin-top:6px}
.f-link{position:absolute;font-size:12px;color:var(--muted)}
.f-label{position:absolute;font-family:"Montserrat",sans-serif;font-weight:700;font-size:12px;color:var(--navy);text-transform:uppercase}
.social{position:absolute;top:4177px;width:24px;height:24px;border-radius:50%;background:var(--navy)}
.copy{position:absolute;left:0;width:1200px;top:4250px;border-top:1px solid #dde2e8;padding-top:12px;text-align:center;font-size:10px;color:var(--muted)}
</style>
</head>
<body>
<div class="page">

  <!-- Hero -->
  <section class="hero" aria-label="Hero and about">
    <div class="ph" role="img" aria-label="Photo of a white grooming van parked in front of a suburban house"
      style="left:593px;top:92px;width:607px;height:643px;border-radius:40px 0 0 0;background:radial-gradient(ellipse at 55% 60%,#f2f5f8 0%,#cfd8e0 40%,rgba(120,140,160,.55) 70%,rgba(40,150,220,0) 100%)"></div>

    <svg class="abs" style="left:34px;top:360px" width="28" height="50" viewBox="0 0 28 50" aria-hidden="true">
      <polyline points="24,2 4,25 24,48" fill="none" stroke="#fff" stroke-width="2.5"/>
    </svg>

    <div class="abs logo">Tailbrook</div>
    <a class="abs nav active" style="left:364px">ABOUT US</a>
    <a class="abs nav" style="left:471px">SERVICES</a>
    <a class="abs nav" style="left:573px">TESTIMONIALS</a>
    <a class="abs nav" style="left:703px">BLOGS</a>
    <a class="abs nav" style="left:789px">CONTACT</a>
    <div class="abs call-pill">CALL US <b>(555) 013-2847</b></div>

    <div class="abs script hero-kicker">Welcome to Tailbrook</div>
    <h1 class="abs hero-title">Doorstep Dog<br>Grooming</h1>
    <p class="abs hero-sub">Mobile Dog Grooming Servicing<br>Los Angeles &amp; Orange County</p>
    <div class="abs btn btn-green" style="left:130px;top:473px;width:167px;height:44px">Book Now</div>

    <!-- About -->
    <div class="ph" role="img" aria-label="Photo of two French bulldog puppies in a wooden tub with towels and shampoo bottles"
      style="left:125px;top:744px;width:460px;height:434px;border-radius:30px;background:radial-gradient(ellipse at 50% 55%,#e8dccb 0%,#c9a77d 38%,rgba(120,200,120,.5) 68%,rgba(60,200,100,0) 100%)"></div>
    <div class="abs script about-kicker">who we are</div>
    <h2 class="abs about-title">About Tailbrook</h2>
    <div class="abs about-text">
      <p>Lorem ipsum dolor sit amet, consectetur adipiscing elit, sed do eiusmod tempor incididunt ut</p>
      <p>Ut enim ad minim veniam, quis nostrud exercitation ullamco laboris nisi ut aliquip ex ea commodo consequat. Duis aute irure dolor in reprehenderi.</p>
    </div>
    <div class="abs btn btn-blue" style="left:632px;top:1113px;width:167px;height:43px">Learn More</div>
    <div class="abs btn btn-outline" style="left:805px;top:1113px;width:166px;height:43px">
      <svg width="13" height="13" viewBox="0 0 24 24" style="margin-right:6px"><path d="M6.6 10.8c1.4 2.8 3.8 5.1 6.6 6.6l2.2-2.2c.3-.3.7-.4 1-.2 1.1.4 2.3.6 3.6.6.6 0 1 .4 1 1V20c0 .6-.4 1-1 1C10.6 21 3 13.4 3 4c0-.6.4-1 1-1h3.5c.6 0 1 .4 1 1 0 1.3.2 2.5.6 3.6.1.3 0 .7-.2 1z" fill="#fff"/></svg>Call Us</div>
  </section>

  <!-- Feature bar -->
  <section class="features" aria-label="Highlights">
    <div class="feat" style="left:156px">
      <svg width="36" height="40" viewBox="0 0 36 40"><path d="M18 3C12 12 6 19 6 26a12 12 0 0 0 24 0C30 19 24 12 18 3z" fill="none" stroke="#fff" stroke-width="2"/><path d="M12 27a6 6 0 0 0 6 6" fill="none" stroke="#fff" stroke-width="2"/></svg>
      <span>Warm<br>Water Bath</span></div>
    <div class="feat" style="left:396px">
      <svg width="44" height="44" viewBox="0 0 44 44"><rect x="22" y="4" width="14" height="20" rx="3" transform="rotate(40 29 14)" fill="none" stroke="#fff" stroke-width="2"/><line x1="22" y1="22" x2="5" y2="40" stroke="#fff" stroke-width="3"/></svg>
      <span>Gentle Brush<br>and Blowout</span></div>
    <div class="feat" style="left:678px">
      <svg width="40" height="46" viewBox="0 0 40 46"><rect x="9" y="16" width="22" height="28" rx="3" fill="none" stroke="#fff" stroke-width="2"/><rect x="15" y="6" width="10" height="10" fill="none" stroke="#fff" stroke-width="2"/><line x1="25" y1="9" x2="34" y2="9" stroke="#fff" stroke-width="2"/><circle cx="20" cy="30" r="5" fill="none" stroke="#fff" stroke-width="2"/></svg>
      <span>All Natural<br>Products</span></div>
    <div class="feat" style="left:906px">
      <svg width="44" height="46" viewBox="0 0 44 46"><circle cx="12" cy="10" r="7" fill="none" stroke="#fff" stroke-width="2"/><circle cx="30" cy="10" r="7" fill="none" stroke="#fff" stroke-width="2"/><line x1="15" y1="16" x2="26" y2="44" stroke="#fff" stroke-width="2"/><line x1="27" y1="16" x2="16" y2="44" stroke="#fff" stroke-width="2"/></svg>
      <span>Trim &amp;<br>File Nails</span></div>
  </section>

  <!-- Video -->
  <section class="video-sec" aria-label="Watch our video">
    <h2 class="abs h-blue" style="left:124px;top:122px;font-size:31px">Watch Our Video</h2>
    <div class="abs body-text" style="left:129px;top:184px;width:360px">
      <p>Lorem ipsum dolor sit amet, consectetur adipiscing elit, sed do eiusmod tempo</p>
      <p>Ut enim ad minim veniam, quis nostrud exercitation ullamco laboris nisi ut aliquip ex ea commodo consequat.</p>
    </div>
    <div class="abs btn btn-green" style="left:124px;top:344px;width:167px;height:44px">Book Now</div>
    <div class="ph" role="img" aria-label="Video still of a groomer blow-drying a Labrador on a table"
      style="left:553px;top:85px;width:525px;height:343px;background:linear-gradient(120deg,#8d8f92 0%,#d5d3cf 45%,#c99a5e 62%,#5d4038 100%)"></div>
    <svg class="abs" style="left:778px;top:220px" width="76" height="76" viewBox="0 0 76 76" aria-label="Play video">
      <circle cx="38" cy="38" r="35" fill="rgba(255,255,255,.15)" stroke="#fff" stroke-width="4"/>
      <polygon points="30,23 55,38 30,53" fill="#fff"/>
    </svg>
  </section>

  <!-- Services -->
  <section aria-label="Our services">
    <h2 class="abs sec-title" style="left:0;width:1214px;top:1910px">Our <span>Services</span></h2>
    <div class="svc green" style="left:122px;top:1980px">
      <div class="ic"><svg width="44" height="44" viewBox="0 0 44 44"><circle cx="22" cy="18" r="9" fill="none" stroke="#fff" stroke-width="2"/><path d="M8 40c2-10 26-10 28 0" fill="none" stroke="#fff" stroke-width="2"/></svg></div>
      <h3>Bath with Shampoo<br>and Conditioner</h3>
      <p>Lorem ipsum dolor sit amet, consectetur adipiscing .</p>
    </div>
    <div class="svc green" style="left:589px;top:1980px">
      <div class="ic"><svg width="44" height="44" viewBox="0 0 44 44"><path d="M8 10l6 6v10c0 8 4 12 8 12s8-4 8-12V16l6-6" fill="none" stroke="#fff" stroke-width="2"/><circle cx="17" cy="22" r="2" fill="#fff"/><circle cx="27" cy="22" r="2" fill="#fff"/></svg></div>
      <h3>Eyes &amp; Ears<br>Cleaning</h3>
      <p>Lorem ipsum dolor sit amet, consectetur adipiscing .</p>
    </div>
    <div class="svc blue" style="left:357px;top:1980px">
      <div class="ic"><svg width="44" height="44" viewBox="0 0 44 44"><rect x="6" y="6" width="16" height="6" fill="none" stroke="#fff" stroke-width="2"/><path d="M18 22c0-5 10-5 10 0 6 0 8 6 4 10H14c-4-4-2-10 4-10z" fill="none" stroke="#fff" stroke-width="2"/></svg></div>
      <h3>Full Body Trimming<br>and Styling</h3>
      <p>Lorem ipsum dolor sit amet, consectetur adipiscing .</p>
    </div>
    <div class="svc blue" style="left:817px;top:1980px">
      <div class="ic"><svg width="44" height="44" viewBox="0 0 44 44"><circle cx="22" cy="24" r="12" fill="none" stroke="#fff" stroke-width="2"/><path d="M14 10l4 6M30 10l-4 6" stroke="#fff" stroke-width="2"/><circle cx="18" cy="23" r="1.8" fill="#fff"/><circle cx="26" cy="23" r="1.8" fill="#fff"/></svg></div>
      <h3>Breed Specific Pro<br>Grooming</h3>
      <p>Lorem ipsum dolor sit amet, consectetur adipiscing .</p>
    </div>
  </section>

  <!-- Why -->
  <section aria-label="Why Tailbrook">
    <svg class="abs" style="left:0;top:2323px" width="1200" height="531" viewBox="0 0 1200 531" aria-hidden="true">
      <rect width="1200" height="531" fill="#36b84f"/>
      <path d="M0 0H584C640 120 640 330 478 531H0Z" fill="#1a86f0"/>
    </svg>
    <div class="ph" role="img" aria-label="Photo of a Yorkshire terrier having its paw held by a groomer"
      style="left:0;top:2323px;width:590px;height:531px;clip-path:path('M0 0H556C604 120 604 330 446 531H0Z');background:linear-gradient(135deg,#f3ece8 0%,#d8c3b4 40%,#9e7a63 65%,#c2326a 100%)"></div>
    <h2 class="abs why-title">Why Tailbrook</h2>
    <p class="abs why-text">Lorem ipsum dolor sit amet, consectetur adipiscing elit, sed do eiusmod tempor incididunt ut labore et dolore.</p>
    <div class="why-item" style="left:686px;top:2559px"><div class="why-ic"><svg width="30" height="34" viewBox="0 0 36 40"><path d="M18 3C12 12 6 19 6 26a12 12 0 0 0 24 0C30 19 24 12 18 3z" fill="none" stroke="#1a86f0" stroke-width="2.5"/></svg></div><span>Warm<br>Water Bath</span></div>
    <div class="why-item" style="left:905px;top:2559px"><div class="why-ic"><svg width="34" height="34" viewBox="0 0 44 44"><rect x="22" y="4" width="14" height="20" rx="3" transform="rotate(40 29 14)" fill="none" stroke="#1a86f0" stroke-width="2.5"/><line x1="22" y1="22" x2="5" y2="40" stroke="#1a86f0" stroke-width="3"/></svg></div><span>Gentle Brush<br>and Blowout</span></div>
    <div class="why-item" style="left:686px;top:2660px"><div class="why-ic"><svg width="30" height="36" viewBox="0 0 40 46"><rect x="9" y="16" width="22" height="28" rx="3" fill="none" stroke="#1a86f0" stroke-width="2.5"/><rect x="15" y="6" width="10" height="10" fill="none" stroke="#1a86f0" stroke-width="2.5"/></svg></div><span>All Natural<br>Products</span></div>
    <div class="why-item" style="left:902px;top:2660px"><div class="why-ic"><svg width="32" height="36" viewBox="0 0 44 46"><circle cx="12" cy="10" r="7" fill="none" stroke="#1a86f0" stroke-width="2.5"/><circle cx="30" cy="10" r="7" fill="none" stroke="#1a86f0" stroke-width="2.5"/><line x1="15" y1="16" x2="26" y2="44" stroke="#1a86f0" stroke-width="2.5"/><line x1="27" y1="16" x2="16" y2="44" stroke="#1a86f0" stroke-width="2.5"/></svg></div><span>Trim &amp;<br>File Nails</span></div>
  </section>

  <!-- Testimonials -->
  <section aria-label="Customer testimonials">
    <h2 class="abs sec-title" style="left:117px;top:2960px;font-size:31px;text-align:left">What <span>Our Customer Says</span></h2>
    <div class="card" style="left:120px;top:3030px">
      <p>Lorem ipsum dolor sit amet, consectetur adipiscing elit, sed do eiusmod tempor incididunt ut labore et dolore magna aliqua. Ut enim ad minim veniam, quis nostrud exercitation ullamco laboris nisi ut aliquiseiusmod tempor incididunt ut labore</p>
      <div class="avatar" role="img" aria-label="Customer portrait"></div>
      <div class="who">Marla Denby</div><div class="stars">★★★★★</div>
    </div>
    <div class="card" style="left:456px;top:3030px">
      <p>Lorem ipsum dolor sit amet, consectetur adipiscing elit, sed do eiusmod tempor incididunt ut labore et dolore magna aliqua. Ut enim ad minim veniam, quis nostrud exercitation ullamco laboris nisi ut aliquiseiusmod tempor incididunt ut labore</p>
      <div class="avatar" role="img" aria-label="Customer portrait"></div>
      <div class="who">Marla Denby</div><div class="stars">★★★★★</div>
    </div>
    <div class="ph" role="img" aria-label="Photo of a Labrador lying under a blue towel beside a basket of grooming tools"
      style="left:769px;top:2941px;width:417px;height:359px;border-radius:40px;background:radial-gradient(ellipse at 55% 55%,#d9a86a 0%,#2f6fc8 45%,rgba(60,110,190,.35) 70%,rgba(255,255,255,0) 100%)"></div>
  </section>

  <!-- Booking -->
  <section class="book" aria-label="Book online">
    <svg class="abs" style="left:0;top:0" width="1200" height="568" aria-hidden="true">
      <path d="M0 568V360h40v-80h50v120h60v-60h70v150h880v-110h40v-90h60v268Z" fill="rgba(255,255,255,.08)"/>
    </svg>
  </section>
  <h2 class="abs book-title">Book Onlie Grooming Service</h2>
  <p class="abs book-text">Lorem ipsum dolor sit amet, consectetur adipiscing elit, sed do eiusmod tempor incididunt ut labore et dolore.Lorem ipsum dolor sit amet, consectetur adipiscing elit, sed do eiusmod</p>
  <div class="abs btn btn-green" style="left:421px;top:3570px;width:166px;height:41px">Learn More</div>
  <div class="abs btn btn-navy" style="left:593px;top:3570px;width:167px;height:41px">
    <svg width="13" height="13" viewBox="0 0 24 24" style="margin-right:6px"><path d="M6.6 10.8c1.4 2.8 3.8 5.1 6.6 6.6l2.2-2.2c.3-.3.7-.4 1-.2 1.1.4 2.3.6 3.6.6.6 0 1 .4 1 1V20c0 .6-.4 1-1 1C10.6 21 3 13.4 3 4c0-.6.4-1 1-1h3.5c.6 0 1 .4 1 1 0 1.3.2 2.5.6 3.6.1.3 0 .7-.2 1z" fill="#fff"/></svg>Call Us</div>

  <!-- Footer -->
  <footer class="footer" aria-label="Footer"></footer>
  <div class="ph" role="img" aria-label="Photo of three small dogs wrapped in pink, blue and yellow towels beside a white grooming van"
    style="left:92px;top:3618px;width:1061px;height:330px;border-radius:60px 60px 30px 30px;background:linear-gradient(90deg,rgba(230,80,150,.85) 0%,#c98a5c 22%,#2aa6e8 38%,#f0c640 55%,#e9eef3 72%,#d3dae2 100%)"></div>

  <div class="abs f-head" style="left:169px;top:4008px">NAVIGATION</div>
  <span class="f-link" style="left:172px;top:4057px">Home</span>
  <span class="f-link" style="left:172px;top:4083px">About Us</span>
  <span class="f-link" style="left:172px;top:4109px">Grooming Services</span>
  <span class="f-link" style="left:172px;top:4135px">Why We Are</span>
  <span class="f-link" style="left:331px;top:4057px">Testimonials</span>
  <span class="f-link" style="left:331px;top:4083px">Book Online Now</span>
  <span class="f-link" style="left:331px;top:4109px">Blogs</span>
  <span class="f-link" style="left:331px;top:4135px">Contact Us</span>
  <span class="social" style="left:180px"></span>
  <span class="social" style="left:210px"></span>
  <span class="social" style="left:242px"></span>

  <div class="abs f-head" style="left:535px;top:4011px">LOCATION WE SERVE</div>
  <span class="f-link" style="left:537px;top:4057px">Lorem ipsum dolor</span>
  <span class="f-link" style="left:537px;top:4083px">Sit amet consectetur</span>
  <span class="f-link" style="left:537px;top:4109px">Adipiscing elit</span>
  <span class="f-link" style="left:537px;top:4135px">Eed do eiusmod</span>
  <span class="f-link" style="left:537px;top:4161px">Tempor</span>

  <div class="abs f-head" style="left:825px;top:4008px">CONTACT US</div>
  <svg class="abs" style="left:824px;top:4056px" width="30" height="30" viewBox="0 0 24 24" aria-hidden="true"><path d="M6.6 10.8c1.4 2.8 3.8 5.1 6.6 6.6l2.2-2.2c.3-.3.7-.4 1-.2 1.1.4 2.3.6 3.6.6.6 0 1 .4 1 1V20c0 .6-.4 1-1 1C10.6 21 3 13.4 3 4c0-.6.4-1 1-1h3.5c.6 0 1 .4 1 1 0 1.3.2 2.5.6 3.6.1.3 0 .7-.2 1z" fill="none" stroke="#1a86f0" stroke-width="1.5"/></svg>
  <span class="f-label" style="left:864px;top:4057px">Phone Number</span>
  <span class="f-link" style="left:864px;top:4080px">(555) 013-2847</span>
  <svg class="abs" style="left:821px;top:4116px" width="32" height="32" viewBox="0 0 32 32" aria-hidden="true"><circle cx="15" cy="17" r="12" fill="none" stroke="#1a86f0" stroke-width="2"/><polyline points="9,17 14,22 29,5" fill="none" stroke="#1a86f0" stroke-width="2"/></svg>
  <span class="f-label" style="left:864px;top:4121px">Working Hours</span>
  <span class="f-link" style="left:864px;top:4142px">Mon- Fri: 7:00 Am to 9:00 Pm</span>
  <span class="f-link" style="left:864px;top:4165px">Sat-Sun: 8:00 Am to 5:00 Pm</span>

  <div class="copy">© 2020 Tailbrook All Rights Reserved</div>
</div>
</body>
</html>
```